Lumora Studio
Business Card, Letterhead, Envelope, Fax
Professional
Marcus Pellway
President / CEO, Lumora Studio
41B W Alder Road, Suite 6
PO Box 7382
Harlow Bend, Vermont 30912
marcus@lumoraweb.example
www.lumoraweb.example
We would also like stationary (letterhead, business card, fax, and envelope - window and windowless).
Please also include QTA Accreditation logo that was uploaded.
Please provide these with an editable format, preferrably Microsoft Word - so that we can create more for additional staff.
Logo and web address (www.lumoraweb.example)
Services can be included (optional)
Web Design and Development
Internet Marketing
E-mail Marketing
Content Management Systems
Graphic and Print Design
Application Development
Consulting
Search Engine Optimization
E-Commerce
QTA Accreditation logo to be included
eps(vector) on white background
ai(vector) on white background
eps (vector) vertical on white background
ai(vector) vertical on white background

```html
<!DOCTYPE html>
<html lang="en">
<head>
<meta charset="utf-8">
<title>Lumora Studio Stationery</title>
<link rel="stylesheet" href="https://fonts.googleapis.com/css2?family=Open+Sans:wght@400;600&display=swap">
<style>
:root{
  --bg:#e4e4e2;
  --paper:#ffffff;
  --paper-shade:#f1f2f4;
  --navy:#1d3a6b;
  --blue:#2f5e9a;
  --blue-light:#6f93c4;
  --text:#5c5f66;
  --faint:#e9ecf0;
  --badge:#2f5e9a;
}
*{margin:0;padding:0;box-sizing:border-box}
html,body{width:1200px;height:901px;overflow:hidden;background:var(--bg);font-family:"Open Sans",sans-serif;color:var(--text)}
.canvas{position:relative;width:1200px;height:901px}
.piece{position:absolute;background:linear-gradient(135deg,var(--paper) 55%,var(--paper-shade));box-shadow:0 3px 10px rgba(0,0,0,.18);overflow:hidden}
.brand{display:flex;align-items:center;gap:6px}
.brand-dot{border-radius:50%;background:var(--blue);flex:none}
.brand-name{font-weight:600;color:var(--navy);white-space:nowrap;letter-spacing:-.2px}
.tagline{color:var(--text);white-space:nowrap}
.faint-circle{position:absolute;border-radius:50%;background:var(--faint)}
.badge{position:absolute;background:var(--badge);border-radius:2px}

/* business card front */
.card-front{left:127px;top:151px;width:192px;height:102px}
.card-front .brand{position:absolute;left:50%;top:18px;transform:translateX(-50%);flex-direction:column;gap:3px}
.card-front .brand-dot{width:22px;height:22px}
.card-front .brand-name{font-size:14px}
.card-front .tagline{font-size:5px;text-align:center}
.card-front .band{position:absolute;left:0;right:0;bottom:10px;height:6px;background:linear-gradient(90deg,var(--navy),var(--blue-light))}

/* business card back */
.card-back{left:348px;top:151px;width:192px;height:109px}
.card-back .brand{position:absolute;left:12px;top:14px;flex-direction:column;align-items:flex-start;gap:2px}
.card-back .brand-dot{width:16px;height:16px}
.card-back .brand-name{font-size:10px}
.card-back .tagline{font-size:4px}
.card-back .contact{position:absolute;left:98px;top:14px;font-size:5.2px;line-height:8px;white-space:nowrap}
.card-back .person{position:absolute;left:12px;top:72px;font-size:5.5px;line-height:8px}
.card-back .person strong{color:var(--navy);font-weight:600}
.card-back .badge{right:12px;bottom:10px;width:14px;height:10px}

/* letterhead */
.letterhead{left:565px;top:134px;width:433px;height:645px}
.letterhead .brand{position:absolute;left:50%;top:28px;transform:translateX(-50%);flex-direction:column;gap:4px}
.letterhead .brand-dot{width:26px;height:26px}
.letterhead .brand-name{font-size:19px}
.letterhead .tagline{font-size:5.5px;text-align:center}
.letterhead .rule{position:absolute;left:30px;right:30px;top:112px;height:1px;background:linear-gradient(90deg,transparent,var(--blue) 30%,var(--blue) 70%,transparent)}
.letterhead .faint-circle{right:-90px;bottom:60px;width:330px;height:330px}
.letterhead .footer{position:absolute;left:30px;bottom:18px;font-size:5.5px;line-height:8px}
.letterhead .badge{right:20px;bottom:20px;width:22px;height:14px}

/* envelopes */
.envelope{width:577px}
.envelope .brand{position:absolute;left:16px;top:14px;gap:7px}
.envelope .brand-dot{width:28px;height:28px}
.envelope .brand-name{font-size:20px}
.envelope .tagline{font-size:5px;margin-top:-2px}
.envelope .return{position:absolute;left:16px;top:52px;font-size:6.5px;white-space:nowrap}
.envelope .band{position:absolute;right:0;top:0;height:100%;width:90px}
.envelope .faint-circle{width:260px;height:260px;right:30px;top:60px}
.env-plain{left:129px;top:316px;height:234px}
.env-window{left:146px;top:443px;height:258px}
.env-window .window{position:absolute;left:16px;top:120px;width:240px;height:82px;border:1px solid #c9ccd2;border-radius:6px;background:#fafbfc}
.env-window .badge{left:272px;top:184px;width:30px;height:14px}
</style>
</head>
<body>
<main class="canvas">

  <section class="piece card-front" aria-label="Business card front">
    <div class="brand">
      <span class="brand-dot"></span>
      <span class="brand-name">Lumora Studio</span>
      <span class="tagline">Creative Web and Print Studio</span>
    </div>
    <div class="band"></div>
  </section>

  <section class="piece card-back" aria-label="Business card back">
    <div class="brand">
      <span class="brand-dot"></span>
      <span class="brand-name">Lumora Studio</span>
      <span class="tagline">Creative Web and Print Studio</span>
    </div>
    <div class="contact">
      41B W Alder Road, Suite 6<br>
      PO Box 7382<br>
      Harlow Bend, Vermont 30912<br>
      Phone 706.555.0142<br>
      Fax 706.555.0187<br>
      Toll Free 800.555.0163
    </div>
    <div class="person">
      <strong>Marcus Pellway</strong><br>
      President / CEO<br>
      marcus@lumoraweb.example
    </div>
    <span class="badge" role="img" aria-label="QTA accreditation badge"></span>
  </section>

  <section class="piece letterhead" aria-label="Letterhead">
    <div class="brand">
      <span class="brand-dot"></span>
      <span class="brand-name">Lumora Studio</span>
      <span class="tagline">Creative Web and Print Studio</span>
    </div>
    <div class="rule"></div>
    <div class="faint-circle"></div>
    <div class="footer">
      41B W Alder Road, Suite 6 · PO Box 7382 · Harlow Bend, Vermont 30912<br>
      Toll Free 800.555.0163 · Phone 706.555.0142 · Fax 706.555.0187<br>
      www.lumoraweb.example
    </div>
    <span class="badge" role="img" aria-label="QTA accreditation badge"></span>
  </section>

  <section class="piece envelope env-plain" aria-label="Envelope">
    <div class="faint-circle"></div>
    <div class="brand">
      <span class="brand-dot"></span>
      <div>
        <div class="brand-name">Lumora Studio</div>
        <div class="tagline">Creative Web and Print Studio</div>
      </div>
    </div>
    <div class="return">41B W Alder Road, Suite 6 · PO Box 7382 · Harlow Bend, Vermont 30912</div>
    <svg class="band" viewBox="0 0 90 234" preserveAspectRatio="none" aria-hidden="true">
      <defs>
        <linearGradient id="bandA" x1="0" x2="1">
          <stop offset="0" stop-color="#6f93c4"/>
          <stop offset=".45" stop-color="#2f5e9a"/>
          <stop offset="1" stop-color="#1d3a6b"/>
        </linearGradient>
      </defs>
      <path d="M40 0 H90 V234 H40 Q20 117 40 0 Z" fill="url(#bandA)"/>
    </svg>
  </section>

  <section class="piece envelope env-window" aria-label="Window envelope">
    <div class="faint-circle"></div>
    <div class="brand">
      <span class="brand-dot"></span>
      <div>
        <div class="brand-name">Lumora Studio</div>
        <div class="tagline">Creative Web and Print Studio</div>
      </div>
    </div>
    <div class="return">41B W Alder Road, Suite 6 · PO Box 7382 · Harlow Bend, Vermont 30912</div>
    <div class="window"></div>
    <span class="badge" role="img" aria-label="QTA accreditation badge"></span>
    <svg class="band" viewBox="0 0 90 258" preserveAspectRatio="none" aria-hidden="true">
      <defs>
        <linearGradient id="bandB" x1="0" x2="1">
          <stop offset="0" stop-color="#6f93c4"/>
          <stop offset=".45" stop-color="#2f5e9a"/>
          <stop offset="1" stop-color="#1d3a6b"/>
        </linearGradient>
      </defs>
      <path d="M40 0 H90 V258 H40 Q20 129 40 0 Z" fill="url(#bandB)"/>
    </svg>
  </section>

</main>
</body>
</html>
```